Site Update/Merger: Darvik Systems

We want to take some content (not ALL the content, but only what is specified) from two or our sites and combine into one
The New Website is in Wordpress too.
The new site needs to be a nice merge between these sites:
◦ https://tovaro-works.example/
◦ https://helmstrand-plan.example/
Theme/topic: this is an Engineering site
The blog must be included on the home page (maybe smaller), and also on the Systems Engineering page (maybe a little bigger, allow the user to browse through all blogs)
Instructions and visual aids:
Step 1: SEE BRIEFING IN THE PDF ATTACHED
Step 2: some pictures for your reference (referenced in the PDF)
Updates
The design of the children pages are not ready, and the designer still needs to load everything into my wordpress site.
Look and feel
Each slider illustrates characteristics of the customer's brand and the style your logo design should communicate.

```html
<!DOCTYPE html>
<html lang="en">
<head>
<meta charset="utf-8">
<title>Darvik Systems — Home</title>
<link href="https://fonts.googleapis.com/css2?family=Roboto:wght@400;500;700&display=swap" rel="stylesheet">
<style>
:root{
  --orange:#f26a0f;
  --blue:#2e8fd8;
  --ink:#111111;
  --text:#333333;
  --muted:#666666;
  --light:#f6f6f6;
  --black:#070707;
  --white:#ffffff;
}
*{margin:0;padding:0;box-sizing:border-box}
html,body{width:1200px;height:2735px;overflow:hidden}
body{font-family:"Roboto",Arial,sans-serif;color:var(--text);background:var(--white);position:relative}
.wrap{width:1000px;margin:0 auto;position:relative}

/* header */
.site-header{height:75px;display:flex;align-items:center}
.site-header .wrap{display:flex;align-items:center;justify-content:space-between}
.brand{font-weight:700;font-size:26px;color:var(--orange);letter-spacing:1px}
.nav{display:flex;align-items:center;gap:44px;font-size:17px;font-weight:500;color:var(--ink);margin-left:auto;margin-right:28px}
.nav .active{color:var(--blue)}
.contact-chip{display:flex;align-items:center;gap:10px}
.contact-chip .icon{width:44px;height:44px;border-radius:50%;background:var(--blue);display:flex;align-items:center;justify-content:center}
.contact-chip small{display:block;font-size:14px;color:var(--text)}
.contact-chip strong{display:block;font-size:17px;font-weight:500;color:var(--ink)}

/* hero */
.hero{height:438px;background:linear-gradient(120deg,#0b3a66 0%,#1c6aa8 40%,#4aa6d9 70%,#10456f 100%);color:var(--white);position:relative}
.hero .wrap{padding-top:107px}
.hero h1{font-size:57px;font-weight:700;line-height:1}
.hero p{font-size:18.5px;font-weight:500;line-height:27px;width:390px;margin-top:16px}
.btn{display:inline-block;background:var(--orange);color:var(--white);font-size:15px;font-weight:700;border-radius:24px;width:168px;height:48px;line-height:48px;text-align:center;margin-top:20px}

/* intro */
.intro{height:325px}
.intro .wrap{display:flex;justify-content:space-between;padding-top:60px}
.intro h2{font-size:42px;font-weight:700;line-height:49px;color:var(--ink);width:500px}
.intro .what{width:470px;padding-top:6px}
.eyebrow{font-size:27px;font-weight:700;color:var(--orange)}
.intro .what p{font-size:16.5px;line-height:31.5px;margin-top:14px;color:var(--text)}

/* services */
.services{height:543px;position:relative;background:var(--light)}
.services .photo{position:absolute;right:0;top:0;width:700px;height:100%;background:linear-gradient(90deg,#f6f6f6 0%,#c7c4be 25%,#8f8a83 55%,#3d3a38 100%)}
.services .wrap{padding-top:73px}
.services h3.eyebrow{font-size:24px}
.services .lead{font-size:16px;font-weight:500;line-height:26px;color:var(--ink);width:420px;margin-top:8px}
.services h4{font-size:19.5px;font-weight:700;color:var(--orange);margin-top:16px}
.services .focus{font-size:16px;color:var(--ink);margin-top:4px}
.feature{display:flex;gap:8px;margin-top:22px;width:420px}
.feature .badge{flex:0 0 56px;width:56px;height:56px;border-radius:50%;background:var(--orange);display:flex;align-items:center;justify-content:center}
.feature h5{font-size:18px;font-weight:500;color:var(--orange);margin-top:2px}
.feature p{font-size:13.5px;line-height:21px;color:var(--ink);margin-top:2px}

/* physics */
.physics{height:450px;position:relative}
.physics .model{position:absolute;left:70px;top:50px;width:520px;height:340px;background:radial-gradient(ellipse at center,#8aa0c8 0%,#c8d2e2 45%,#ffffff 75%)}
.physics .text{position:absolute;left:654px;top:128px;width:460px}
.physics h3{font-size:29px;font-weight:500;line-height:32px;color:var(--ink)}
.physics p{font-size:15.5px;line-height:32px;margin-top:16px;color:var(--text)}

/* blogs */
.blogs{height:632px;background:var(--light)}
.blogs h2{text-align:center;font-size:38px;font-weight:700;color:var(--ink);padding-top:73px}
.cards{display:flex;justify-content:space-between;margin-top:28px}
.card{width:320px;height:400px;background:var(--white);padding:6px;position:relative}
.card .thumb{height:206px;position:relative}
.card .date{position:absolute;left:72px;bottom:-2px;width:164px;height:36px;background:var(--orange);color:var(--white);font-size:14px;display:flex;align-items:center;justify-content:center;gap:6px}
.card .body{padding:18px 4px 0}
.card h3{font-size:17px;font-weight:700;line-height:22px;color:var(--ink)}
.card p{font-size:13px;line-height:21.5px;color:var(--muted);margin-top:10px}
.card .more{font-size:13px;font-weight:500;color:var(--orange);margin-top:6px;display:block}

/* footer */
.site-footer{height:272px;background:var(--black);color:var(--white);text-align:center}
.site-footer .brand{display:block;padding-top:82px;font-size:34px}
.site-footer .info{font-size:15px;margin-top:44px;display:flex;justify-content:center;align-items:center;gap:22px}
.site-footer .info span{display:flex;align-items:center;gap:6px}
.site-footer .copy{font-size:15px;margin-top:30px}
</style>
</head>
<body>

<header class="site-header">
  <div class="wrap">
    <span class="brand">DARVIK SYSTEMS</span>
    <nav class="nav">
      <span class="active">HOME</span><span>|</span><span>SERVICES</span><span>|</span><span>CONTACT US</span>
    </nav>
    <div class="contact-chip">
      <span class="icon"><svg width="22" height="16" viewBox="0 0 22 16"><rect x="1" y="1" width="20" height="14" fill="none" stroke="#fff" stroke-width="1.6"/><path d="M1 1l10 8 10-8" fill="none" stroke="#fff" stroke-width="1.6"/></svg></span>
      <div><small>Email Us</small><strong>info@helmstrand-plan.example</strong></div>
    </div>
  </div>
</header>

<section class="hero" role="img" aria-label="Close-up photo of a blue circuit board with chips and capacitors">
  <div class="wrap">
    <h1>WHO WE ARE</h1>
    <p>A Multi-Disciplinary Consulting &amp; Engineering Service Provider for theEV Industry and e-Mobility</p>
    <span class="btn">GET STARTED</span>
  </div>
</section>

<section class="intro">
  <div class="wrap">
    <h2>SYSTEMS ENGINEERING SOLUTIONS MODELING AND HARDWARE IN THE LOOP CONSULTING</h2>
    <div class="what">
      <h3 class="eyebrow">WHAT WE DO</h3>
      <p>&nbsp;A team of automotive, control and mechanical engineers from different industries and backgrounds and with &nbsp;more than 10 years of experience that came together to provide cost effective and specialized services to your &nbsp;organization or team in the pursue of your projects goals.</p>
    </div>
  </div>
</section>

<section class="services">
  <div class="photo" role="img" aria-label="Photo of an engineer with a laptop working at a server rack full of cables"></div>
  <div class="wrap">
    <h3 class="eyebrow">OUR SERVICES</h3>
    <p class="lead">This is just a glance at the activities and projects we can contribute to.For more details, go to our services menu or contact us to have a</p>
    <h4>SYSTEMS ENGINEERING</h4>
    <p class="focus">Our Focus: Collaboration, Accountability and Feedback</p>
    <div class="feature">
      <span class="badge"><svg width="30" height="30" viewBox="0 0 30 30" fill="#fff"><circle cx="15" cy="9" r="4"/><circle cx="7" cy="12" r="3"/><circle cx="23" cy="12" r="3"/><path d="M8 24c0-5 3-8 7-8s7 3 7 8z"/><path d="M2 23c0-4 2-6 5-6 1 0 2 0 2 1-1 1-2 3-2 5z"/><path d="M28 23c0-4-2-6-5-6-1 0-2 0-2 1 1 1 2 3 2 5z"/></svg></span>
      <div><h5>COLLABORATION</h5><p>Working together is the only way to &nbsp;maximize the team’s potential</p></div>
    </div>
    <div class="feature">
      <span class="badge"><svg width="26" height="30" viewBox="0 0 26 30"><rect x="3" y="4" width="20" height="24" rx="2" fill="none" stroke="#fff" stroke-width="2.4"/><rect x="9" y="1" width="8" height="5" rx="1" fill="#fff"/><path d="M7 13h3M13 13h7M7 18h3M13 18h7M7 23h3M13 23h7" stroke="#fff" stroke-width="2"/></svg></span>
      <div><h5>ACCOUNTABILITY</h5><p>Individual contributions are paramount to the team’s success</p></div>
    </div>
    <div class="feature">
      <span class="badge"><svg width="30" height="30" viewBox="0 0 30 30" fill="#fff"><path d="M5 3l1 2 2 .3-1.5 1.4.4 2.1L5 7.8 3.1 8.8l.4-2.1L2 5.3 4 5z"/><path d="M15 3l1 2 2 .3-1.5 1.4.4 2.1L15 7.8l-1.9 1 .4-2.1L12 5.3l2-.3z"/><path d="M25 3l1 2 2 .3-1.5 1.4.4 2.1-1.9-1-1.9 1 .4-2.1L22 5.3l2-.3z"/><rect x="3" y="16" width="5" height="11"/><path d="M10 16l5-5c1-1 3 0 2 2l-1 3h8c2 0 2 3 0 3 2 0 2 3 0 3 1.5 0 1.5 3-.5 3H10z"/></svg></span>
      <div><h5>FEEDBACK</h5><p>Clear Feedback methods are in place</p></div>
    </div>
  </div>
</section>

<section class="physics">
  <div class="model" role="img" aria-label="Illustration of an exploded car showing body, seats, engine and wheels"></div>
  <div class="text">
    <h3>PHYSICS-BASED MODELING AND HARDWARE IN THE LOOP</h3>
    <p>From data-driven system identification to real-time mathematical models &nbsp;for your simulation; we can handle that work for you. In addition, we are &nbsp;highly skilled on HIL testing and can support you in design and build &nbsp;phases to satisfy complex validation testing.</p>
  </div>
</section>

<section class="blogs">
  <h2>LATEST BLOGS</h2>
  <div class="wrap cards">
    <article class="card">
      <div class="thumb" role="img" aria-label="Photo of hands holding a green circuit board" style="background:linear-gradient(135deg,#1a1a1a 0%,#3f8a4f 55%,#1b1b1b 100%)">
        <span class="date"><svg width="12" height="12" viewBox="0 0 12 12"><rect x="1" y="2" width="10" height="9" fill="none" stroke="#fff"/><path d="M1 5h10M4 1v2M8 1v2" stroke="#fff"/></svg>JUNE 04,2021</span>
      </div>
      <div class="body">
        <h3>Design And Implementation<br>(The “how”)</h3>
        <p>by R. Havel, Helmstrand Plan Team Follow the “what”, the “how”, and the “validation” as we navigate the ins and outs of the so-called</p>
        <span class="more">READ MORE ▸</span>
      </div>
    </article>
    <article class="card">
      <div class="thumb" role="img" aria-label="Photo of engineers working in a vehicle assembly workshop" style="background:linear-gradient(135deg,#d9dde0 0%,#8e9497 50%,#3c3f42 100%)">
        <span class="date"><svg width="12" height="12" viewBox="0 0 12 12"><rect x="1" y="2" width="10" height="9" fill="none" stroke="#fff"/><path d="M1 5h10M4 1v2M8 1v2" stroke="#fff"/></svg>JUNE 04,2021</span>
      </div>
      <div class="body">
        <h3>What Is The Design Process And Why Is The System Broken?</h3>
        <p>by R. Havel, Helmstrand Plan Team Follow the “what”, the “how”, and the “validation” as we navigate the ins and outs of the so-called</p>
        <span class="more">READ MORE ▸</span>
      </div>
    </article>
    <article class="card">
      <div class="thumb" role="img" aria-label="Illustration of a glowing purple microchip on a circuit board" style="background:radial-gradient(circle at center,#d7b6ee 0%,#7a4fc0 35%,#2a1f6e 75%)">
        <span class="date"><svg width="12" height="12" viewBox="0 0 12 12"><rect x="1" y="2" width="10" height="9" fill="none" stroke="#fff"/><path d="M1 5h10M4 1v2M8 1v2" stroke="#fff"/></svg>JUNE 04,2021</span>
      </div>
      <div class="body">
        <h3>How To Approach Requirement Definition In The Design Process</h3>
        <p>by R. Havel, Helmstrand Plan Team Follow the “what”, the “how”, and the “validation” as we navigate the ins and outs of the so-called</p>
        <span class="more">READ MORE ▸</span>
      </div>
    </article>
  </div>
</section>

<footer class="site-footer">
  <span class="brand">DARVIK SYSTEMS</span>
  <div class="info">
    <span><svg width="10" height="14" viewBox="0 0 10 14"><path d="M5 0a5 5 0 0 1 5 5c0 4-5 9-5 9S0 9 0 5a5 5 0 0 1 5-5z" fill="#fff"/><circle cx="5" cy="5" r="2" fill="#070707"/></svg>North America Location: Ashford Ridge, SC</span>
    <span>|</span>
    <span><svg width="15" height="11" viewBox="0 0 15 11"><rect x=".7" y=".7" width="13.6" height="9.6" fill="none" stroke="#fff" stroke-width="1.3"/><path d="M.7 .7l6.8 5.5 6.8-5.5" fill="none" stroke="#fff" stroke-width="1.3"/></svg>Email: info@helmstrand-plan.example</span>
  </div>
  <p class="copy">DARVIK SYSTEMS © 2021 ALL RIGHTS RESERVED</p>
</footer>

</body>
</html>
```